Business Card Design Project

I own a dental practice and would like to use a logo that was recently designed to make business cards.
I am looking for a clean card with the following information on the card.

Halvorsen Dental Center (Using the logo)
Martin L. Halvorsen, D.D.S.
7234 Pinewick Ave. Suite B
Colorado Springs, CO 80547
(719) 482-6130
halvorsendentalcenter@mailbox-example.net
www.halvorsendentalcenter.example

Also a list of items on the back:
Services include

Family Dentistry
Cosmetic
Whitening
Tooth Colored Fillings
Crowns/Bridges
Implants/Tooth Replacement
Dentures
Root Canals
Updates

Just an FYI, I added an email address and website address.

I also added my Pic.  Please give designs with and without the pic

Thanks

Target Market(s)

20-70 U.S. Female that handles the household budget.

Industry/Entity Type

Dental

Requirements
Must have
• The logo is key. The color scheme of the logo is also key. The back of the business card should have the list of Dental Services offered at the practice. The front should be clean and professional looking. No cartoons. I will also include a picture of myself. I think that the final card may or may not include this picture, so the card designs should come with and without the picture. USE THE BLUE LOGO ONLY!!!
Should not have
• NO teeth should be on the card.

```html
<!DOCTYPE html>
<html lang="en">
<head>
<meta charset="utf-8">
<title>Halvorsen Dental Center — Business Card</title>
<link href="https://fonts.googleapis.com/css2?family=Montserrat:wght@500;600;700&family=Questrial&display=swap" rel="stylesheet">
<style>
  :root {
    --page-bg: #ece7df;
    --card-blue-light: #2aa3cf;
    --card-blue-mid: #1f86b8;
    --card-blue-dark: #1a6694;
    --logo-ink: #e3f0f6;
    --name-ink: #f4f8fb;
    --contact-ink: #d6f1b4;
    --back-bg: #f7fafb;
    --back-ink: #111416;
    --photo-a: #5d6a78;
    --photo-b: #2b323b;
  }
  * { margin: 0; padding: 0; box-sizing: border-box; }
  html, body { width: 1200px; height: 1000px; overflow: hidden; }
  body {
    position: relative;
    background: var(--page-bg);
    font-family: "Montserrat", sans-serif;
  }

  /* Front of card */
  .card-front {
    position: absolute;
    left: 400px; top: 152px;
    width: 568px; height: 326px;
    border-radius: 22px 0 22px 0;
    overflow: hidden;
    background: radial-gradient(ellipse at 38% 50%, var(--card-blue-light) 0%, var(--card-blue-mid) 45%, var(--card-blue-dark) 100%);
    box-shadow: 0 6px 14px rgba(0,0,0,0.25);
  }
  .brand {
    position: absolute;
    left: 30px; top: 76px;
    display: flex; align-items: center; gap: 12px;
  }
  .brand-dot {
    width: 30px; height: 30px;
    border-radius: 50%;
    background: var(--logo-ink);
  }
  .brand-name {
    font-family: "Questrial", sans-serif;
    font-size: 27px;
    color: var(--logo-ink);
    letter-spacing: 0.5px;
  }
  .portrait {
    position: absolute;
    right: 0; top: 0;
    width: 130px; height: 153px;
    background: linear-gradient(160deg, var(--photo-a), var(--photo-b));
  }
  .dentist-name {
    position: absolute;
    right: 20px; top: 156px;
    font-size: 21px; font-weight: 700;
    font-variant: small-caps;
    letter-spacing: 0.5px;
    color: var(--name-ink);
    text-shadow: 0 1px 2px rgba(0,0,0,0.35);
  }
  .contact {
    position: absolute;
    display: flex; align-items: center; gap: 7px;
    font-size: 13px; font-weight: 600;
    color: var(--contact-ink);
    letter-spacing: 0.6px;
  }
  .contact svg { width: 20px; height: 20px; flex: none; }
  .contact-phone { right: 60px; top: 193px; font-size: 14px; }
  .contact-email { left: 20px; top: 250px; font-variant: small-caps; }
  .contact-web { right: 22px; top: 278px; font-variant: small-caps; }

  /* Back of card */
  .card-back {
    position: absolute;
    left: 230px; top: 492px;
    width: 575px; height: 338px;
    border-radius: 0 22px 0 22px;
    background: var(--back-bg);
    box-shadow: 0 6px 14px rgba(0,0,0,0.25);
    color: var(--back-ink);
  }
  .services-title {
    position: absolute;
    left: 0; right: 0; top: 28px;
    text-align: center;
    font-size: 19px; font-weight: 700;
    font-variant: small-caps;
  }
  .services-list {
    position: absolute;
    list-style: none;
    top: 76px;
  }
  .services-list li {
    position: relative;
    height: 29px;
    padding-left: 20px;
    font-size: 15px; font-weight: 600;
    font-variant: small-caps;
    line-height: 24px;
  }
  .services-list li::before {
    content: "";
    position: absolute;
    left: 0; top: 8px;
    width: 9px; height: 9px;
    border-radius: 50%;
    background: var(--back-ink);
  }
  .services-left { left: 42px; }
  .services-right { left: 301px; }
  .address {
    position: absolute;
    left: 46px; top: 288px;
    display: flex; align-items: center; gap: 10px;
    font-size: 16px; font-weight: 700;
    font-variant: small-caps;
  }
  .address svg { width: 20px; height: 24px; }
</style>
</head>
<body>

<section class="card-front" aria-label="Card front">
  <div class="brand">
    <span class="brand-dot"></span>
    <span class="brand-name">Halvorsen Dental Center</span>
  </div>
  <div class="portrait" role="img" aria-label="Portrait photo of the dentist"></div>
  <p class="dentist-name">Martin L. Halvorsen, D.D.S.</p>

  <p class="contact contact-phone">
    <svg viewBox="0 0 24 24" aria-hidden="true"><path d="M6.6 3.5l3 3.2-1.8 2.4c1.2 2.6 3.3 4.7 6 6l2.3-1.8 3.3 3-1.8 3c-7.6-.3-13.6-6.4-13.9-14z" fill="none" stroke="currentColor" stroke-width="1.8" stroke-linejoin="round"/></svg>
    (719) 482-6130
  </p>
  <p class="contact contact-email">
    <svg viewBox="0 0 24 24" aria-hidden="true"><circle cx="12" cy="12" r="9" fill="none" stroke="currentColor" stroke-width="2"/><circle cx="12" cy="12" r="3.5" fill="none" stroke="currentColor" stroke-width="2"/></svg>
    halvorsendentalcenter@mailbox-example.net
  </p>
  <p class="contact contact-web">
    <svg viewBox="0 0 24 24" aria-hidden="true"><circle cx="12" cy="12" r="9" fill="none" stroke="currentColor" stroke-width="2"/><path d="M3 12h18M12 3c3 3 3 15 0 18M12 3c-3 3-3 15 0 18" fill="none" stroke="currentColor" stroke-width="1.5"/></svg>
    www.halvorsendentalcenter.example
  </p>
</section>

<section class="card-back" aria-label="Card back">
  <h2 class="services-title">Services :</h2>
  <ul class="services-list services-left">
    <li>Family Dentistry</li>
    <li>Cosmetic</li>
    <li>Whitening</li>
    <li>Tooth Colored Fillings</li>
  </ul>
  <ul class="services-list services-right">
    <li>Dentures</li>
    <li>Crowns/Bridges</li>
    <li>Implants/Tooth Replacement</li>
    <li>Root Canals</li>
  </ul>
  <p class="address">
    <svg viewBox="0 0 20 24" aria-hidden="true"><path d="M10 22s-7-7.5-7-12.5a7 7 0 0 1 14 0C17 14.5 10 22 10 22z" fill="none" stroke="currentColor" stroke-width="2"/><circle cx="10" cy="9.5" r="2.6" fill="none" stroke="currentColor" stroke-width="2"/></svg>
    7234 Pinewick Ave. Suite B Colorado Springs, CO 80547
  </p>
</section>

</body>
</html>
```